Business Card and Logo Color Scheme Design Contest

We are starting a new company called Lonestar Precision Surveying and already have a logo however, the colors for the logo itself are not final and COULD be changed. I'm hoping to move AWAYfrom the gold color in the card and the logo as it seems a bit outdated. What we need help with is to find what our business color scheme will be, and then incorporate those colors into both the logo and the business card design itself. We also want to make sure we are known as "LPS" so in the future we can just refer to ourselves as "LPS" and not Lonestar Precision Surveying. That being said, I would like to make a slight change to the logo to somehow include the letters "LPS." The logo used in the front of the card design MUST ALSO include the words "Firm No. 64307" within the logo. My vision is for the front of the card to have the information shown in the attached image. For the back of the card, I'm hoping to have something very simple. I'm envisioning a solid color with either the website (www.surveyplainsco.com) and a simplified version of the logo. I've attached an example but I'm looking for a complete redesign. I'm looking for a slick, modern and simple design.

Industry/Entity Type

Civil Engineer

Contact Information for Business Card

Logo
Firm No. 64307
Marcus Holloway, PE
Chief Operating Officer
Email:mholloway@surveyplainsco.com
Ph: 936.482.3095 | D: 936.482.3067 | M:210.347.6152
4718 W. Bramwell, Conroe, Texas 77318
www.surveyplainsco.com

Requirements
Must have
• Logo
Contact Info
Nice to have
• "LPS" Incorporated in the design
Should not have
• The current color scheme

```html
<!DOCTYPE html>
<html lang="en">
<head>
<meta charset="utf-8">
<title>Lonestar Precision Surveying — Business Card</title>
<link rel="stylesheet" href="https://fonts.googleapis.com/css2?family=Montserrat:wght@700;800&family=Oswald:wght@500&family=Source+Sans+3:wght@400;600;700&display=swap">
<style>
  :root {
    --navy: #0f2540;
    --paper: #f4f4f4;
    --backdrop: #e3e3e3;
    --grey-text: #5e5e5e;
    --body-text: #4a4a4a;
  }
  * { margin: 0; padding: 0; box-sizing: border-box; }
  html, body { width: 1200px; height: 960px; overflow: hidden; }
  body {
    background: var(--backdrop);
    position: relative;
    font-family: "Source Sans 3", Arial, sans-serif;
  }
  .card {
    position: absolute;
    left: 311px;
    width: 578px;
    height: 331px;
    overflow: hidden;
  }
  .card--back { top: 128px; background: var(--navy); }
  .card--front { top: 509px; background: var(--paper); }

  .map-area { position: absolute; }
  .card--back .map-area {
    left: 0; top: 0; width: 354px; height: 331px;
    background: linear-gradient(160deg, #f6f6f6, #e9e9e9);
  }
  .card--front .map-area {
    left: 344px; top: 30px; width: 210px; height: 273px;
    background: linear-gradient(160deg, #13294a, var(--navy));
    clip-path: polygon(0 0, 100% 0, 100% 100%, 76px 100%, 76px 224px, 0 224px);
  }

  .monogram {
    position: absolute;
    font-family: "Montserrat", Arial, sans-serif;
    font-weight: 800;
    line-height: 1;
    letter-spacing: -2px;
  }
  .card--back .monogram { left: 107px; top: 106px; font-size: 118px; color: var(--navy); }
  .card--front .monogram { left: 354px; top: 118px; font-size: 88px; color: var(--paper); }

  .website {
    position: absolute;
    right: 39px; top: 283px;
    font-size: 15px;
    color: #ffffff;
  }
  .website strong { font-weight: 700; }

  .identity { position: absolute; left: 40px; top: 34px; }
  .company-name {
    font-family: "Montserrat", Arial, sans-serif;
    font-weight: 800;
    font-size: 35px;
    line-height: 1;
    color: var(--navy);
  }
  .company-sub {
    font-family: "Oswald", Arial, sans-serif;
    font-weight: 500;
    font-size: 19px;
    color: var(--grey-text);
    margin-top: 4px;
  }
  .firm-no { font-size: 15px; color: var(--grey-text); margin-top: 1px; }

  .divider {
    position: absolute;
    left: 40px; top: 151px;
    width: 304px; height: 3px;
    background: var(--navy);
  }

  .person { position: absolute; left: 40px; top: 164px; }
  .person-name { font-weight: 700; font-size: 18px; color: var(--navy); letter-spacing: .3px; }
  .person-title { font-size: 15px; color: var(--grey-text); margin-top: 1px; }

  .address { position: absolute; left: 40px; top: 234px; font-size: 15px; color: var(--body-text); }

  .contacts {
    position: absolute;
    left: 40px; top: 261px;
    display: grid;
    grid-template-columns: auto auto;
    column-gap: 12px;
    row-gap: 2px;
    font-size: 15px;
    color: var(--body-text);
  }
  .contact { display: flex; align-items: center; gap: 4px; }
  .contact svg { width: 13px; height: 13px; fill: var(--navy); flex: none; }
</style>
</head>
<body>

  <section class="card card--back" aria-label="Card back">
    <div class="map-area" role="img" aria-label="Outline map of Texas in light grey"></div>
    <div class="monogram">LPS</div>
    <p class="website">www.<strong>surveyplainsco</strong>.com</p>
  </section>

  <section class="card card--front" aria-label="Card front">
    <div class="identity">
      <h1 class="company-name">LONESTAR</h1>
      <p class="company-sub">PRECISION SURVEYING, LLC</p>
      <p class="firm-no">Firm No. 64307</p>
    </div>

    <div class="divider"></div>
    <div class="map-area" role="img" aria-label="Outline map of Texas in navy"></div>
    <div class="monogram">LPS</div>

    <div class="person">
      <h2 class="person-name">MARCUS HOLLOWAY, PE</h2>
      <p class="person-title">Chief Operating Officer</p>
    </div>

    <p class="address">4718 W. Bramwell, Conroe, Texas 77318</p>

    <div class="contacts">
      <span class="contact">
        <svg viewBox="0 0 24 24"><path d="M6.6 10.8a15.1 15.1 0 0 0 6.6 6.6l2.2-2.2a1 1 0 0 1 1-.25 11.4 11.4 0 0 0 3.6.57 1 1 0 0 1 1 1V20a1 1 0 0 1-1 1A17 17 0 0 1 3 4a1 1 0 0 1 1-1h3.5a1 1 0 0 1 1 1c0 1.25.2 2.45.57 3.57a1 1 0 0 1-.25 1z"/></svg>
        936.482.3095
      </span>
      <span class="contact">
        <svg viewBox="0 0 24 24"><path d="M6.6 10.8a15.1 15.1 0 0 0 6.6 6.6l2.2-2.2a1 1 0 0 1 1-.25 11.4 11.4 0 0 0 3.6.57 1 1 0 0 1 1 1V20a1 1 0 0 1-1 1A17 17 0 0 1 3 4a1 1 0 0 1 1-1h3.5a1 1 0 0 1 1 1c0 1.25.2 2.45.57 3.57a1 1 0 0 1-.25 1z"/></svg>
        936.482.3067 (Direct)
      </span>
      <span class="contact">
        <svg viewBox="0 0 24 24"><path d="M7 1h10a2 2 0 0 1 2 2v18a2 2 0 0 1-2 2H7a2 2 0 0 1-2-2V3a2 2 0 0 1 2-2zm0 3v14h10V4zm5 15.2a1.2 1.2 0 1 0 0 2.4 1.2 1.2 0 0 0 0-2.4z"/></svg>
        210.347.6152
      </span>
      <span class="contact">
        <svg viewBox="0 0 24 24"><path d="M2 5h20v14H2zm2 2v.4l8 5.2 8-5.2V7zm0 2.8V17h16V9.8l-8 5.2z"/></svg>
        mholloway@surveyplainsco.com
      </span>
    </div>
  </section>

</body>
</html>
```